ambitious event and festival agency from austria needs fresh business card design

A new design is due for the new headquarters and the new challenges. We organize events for different target groups from 16 to 60 years. The design should therefore be straightforward and not confused, so we are open to new colors and the logo may also be changed. In general, however, the most interesting suggestions are the most interesting ones. after this order we are looking for more graphics for quillvane facebook instagramm homepage etc A new design is due for the new headquarters and the new challenges. We organize events for different target groups from 16 to 60 years. The design should therefore be straightforward and not confused, so we are open to new colors and the logo may also be changed. In general, however, the most interesting suggestions are the most interesting ones. after this order we are looking for more graphics for quillvane facebook instagramm homepage etc A new design is due for the new headquarters and the new challenges. We organize events for different target groups from 16 to 60 years. The design should therefore be straightforward and not confused, so we are open to new colors and the logo may also be changed. In general, however, the most interesting suggestions are the most interesting ones. after this order we are looking for more graphics for quillvane facebook instagramm homepage etc
Updates

Reason: I am sorry for this decision but i need some more time. No new designs please, there are so many good ones and I will have made a decision in the next 3 days.

Target Market(s)

Industry/Entity Type

Business

Font styles to use
Serif
Sans Serif

Colors

Designer to choose colors to be used in the design.

Requirements
Must have
Nice to have
Should not have

```html
<!DOCTYPE html>
<html lang="de">
<head>
<meta charset="utf-8">
<title>quillvane – Visitenkarte</title>
<link rel="stylesheet" href="https://fonts.googleapis.com/css2?family=Lato:wght@300;400;700&display=swap">
<style>
  :root {
    --stage: #ecebe8;
    --red: #c8283f;
    --red-deep: #a81f33;
    --red-light: #d8354d;
    --white: #ffffff;
    --paper: #f6f6f6;
    --grey: #8d9a9c;
    --grey-text: #6f7374;
    --crowd: #e4e4e4;
  }
  html, body {
    margin: 0;
    padding: 0;
    width: 1200px;
    height: 780px;
    overflow: hidden;
    background: var(--stage);
    font-family: "Lato", sans-serif;
  }
  .canvas {
    position: relative;
    width: 1200px;
    height: 780px;
  }
  .card {
    position: absolute;
    top: 235px;
    width: 520px;
    height: 300px;
    border-radius: 18px;
    overflow: hidden;
    box-shadow: 0 10px 28px rgba(0,0,0,0.18);
  }
  .card-front { left: 50px; background: var(--paper); }
  .card-back {
    left: 630px;
    background: radial-gradient(ellipse at 45% 40%, var(--red-light), var(--red-deep));
  }
  .front-band {
    position: absolute;
    left: 0;
    top: 0;
    width: 100%;
    height: 124px;
    background: linear-gradient(90deg, var(--red-deep), var(--red) 60%, var(--red-light));
  }
  .front-rule {
    position: absolute;
    left: 0;
    top: 124px;
    width: 100%;
    height: 6px;
    background: var(--grey);
  }
  .front-logo {
    position: absolute;
    left: 34px;
    top: 30px;
    font-size: 62px;
    font-weight: 700;
    color: var(--white);
    letter-spacing: -1px;
    line-height: 1;
  }
  .crowd {
    position: absolute;
    left: 200px;
    top: 150px;
    width: 260px;
    height: 150px;
    background: linear-gradient(180deg, rgba(228,228,228,0) 0%, var(--crowd) 75%, rgba(228,228,228,0.5) 100%);
  }
  .contact {
    position: absolute;
    left: 30px;
    top: 146px;
    color: var(--grey-text);
    font-size: 12.5px;
    line-height: 1.45;
  }
  .contact-name {
    font-size: 19px;
    line-height: 1.2;
    color: var(--red);
    font-weight: 400;
    margin: 0;
  }
  .contact-role { margin: 0 0 8px; font-size: 14px; }
  .contact-lines { margin: 0 0 8px; }
  .contact-icons { display: flex; gap: 5px; }
  .contact-icons svg { width: 15px; height: 15px; }
  .address {
    position: absolute;
    right: 30px;
    top: 150px;
    text-align: right;
    font-size: 13px;
    line-height: 1.4;
    color: var(--grey-text);
  }
  .address-brand { color: var(--red); }
  .back-crowd {
    position: absolute;
    left: 0;
    top: 0;
    width: 260px;
    height: 300px;
    background: linear-gradient(90deg, rgba(150,20,40,0.25), rgba(150,20,40,0));
  }
  .back-logo {
    position: absolute;
    left: 40px;
    top: 96px;
    font-size: 82px;
    font-weight: 700;
    color: var(--white);
    letter-spacing: -1px;
    line-height: 1;
  }
  .back-url {
    position: absolute;
    left: 44px;
    top: 200px;
    font-size: 15px;
    letter-spacing: 1px;
    color: #f3d6da;
  }
</style>
</head>
<body>
<main class="canvas">

  <section class="card card-front" aria-label="Vorderseite">
    <div class="front-band"></div>
    <div class="front-rule"></div>
    <div class="crowd" role="img" aria-label="Faint silhouettes of a cheering festival crowd"></div>
    <div class="front-logo">quillvane</div>

    <div class="contact">
      <p class="contact-name">Lukas Brandhofer</p>
      <p class="contact-role">Geschäftsführer</p>
      <p class="contact-lines">
        +43 660 418 372 5<br>
        l.brandhofer@quillvane.eu<br>
        www.quillvane.eu
      </p>
      <div class="contact-icons">
        <svg viewBox="0 0 16 16" aria-label="Telefon"><circle cx="8" cy="8" r="7" fill="none" stroke="var(--red)" stroke-width="1.4"/><rect x="5.5" y="4" width="5" height="8" rx="1" fill="none" stroke="var(--red)" stroke-width="1.2"/></svg>
        <svg viewBox="0 0 16 16" aria-label="E-Mail"><circle cx="8" cy="8" r="7" fill="var(--red)"/><path d="M4.5 5.5h7v5h-7z M4.5 5.5l3.5 3 3.5-3" fill="none" stroke="#fff" stroke-width="1.1"/></svg>
        <svg viewBox="0 0 16 16" aria-label="Web"><circle cx="8" cy="8" r="7" fill="none" stroke="var(--red)" stroke-width="1.4"/><circle cx="8" cy="8" r="4" fill="none" stroke="var(--red)" stroke-width="1.1"/><path d="M4 8h8M8 4v8" stroke="var(--red)" stroke-width="1"/></svg>
      </div>
    </div>

    <div class="address">
      <span class="address-brand">quillvane</span><br>
      Birkenau 14<br>
      A4380 Steinfeld
    </div>
  </section>

  <section class="card card-back" aria-label="Rückseite">
    <div class="back-crowd" role="img" aria-label="Faint silhouettes of a cheering crowd"></div>
    <div class="back-logo">quillvane</div>
    <div class="back-url">www.quillvane.eu</div>
  </section>

</main>
</body>
</html>
```